Global E-commerce Business Needs Banner Ad

We need banner ads for a fast growing E-commerce business cater mostly to women. The ads must have unique and beautiful background that accentuate the products. The ads should also have between 1-4 products in it. It needs to have the headline "Up To 80% Off Retail" in the ad. The ad also needs to have our logo and a "View Now" button. The ad should be more feminine and playful. Each product should have a different background design specially for the product to make it more beautiful.

Dimension: 320 by 480 pixel

Target Market(s)

Women

Industry/Entity Type

Business

Requirements
Must have
• 1) "Up To 80% Off Retail"
• 2) Brimvale Logo
• 3) "View Now" button

```html
<!DOCTYPE html>
<html lang="en">
<head>
<meta charset="utf-8">
<title>Brimvale Banner – Up To 80% Off Retail</title>
<link href="https://fonts.googleapis.com/css2?family=Roboto:wght@300;400&family=Roboto+Condensed:wght@400;700&display=swap" rel="stylesheet">
<style>
  :root {
    --stage: #6f6f6f;
    --purple: #5a3994;
    --purple-light: #7653b3;
    --purple-dark: #432874;
    --white: #ffffff;
    --pink: #ec1a80;
    --yellow: #ffe61a;
    --ink: #3a3a3a;
    --ink-soft: #4a4a4a;
    --peach: #fcd9a8;
    --sky: #9bd5ef;
    --blush: #f6b3c4;
  }
  * { box-sizing: border-box; margin: 0; padding: 0; }
  html, body { width: 1200px; height: 1200px; overflow: hidden; }
  body {
    background: radial-gradient(circle at 50% 45%, #8a8a8a 0%, var(--stage) 75%);
    font-family: "Roboto", Arial, sans-serif;
    position: relative;
  }
  .banner {
    position: absolute;
    left: 300px; top: 150px;
    width: 600px; height: 900px;
    overflow: hidden;
    background: radial-gradient(ellipse at 50% 55%, var(--purple-light) 0%, var(--purple) 55%, var(--purple-dark) 100%);
  }
  .header-wave { position: absolute; left: 0; top: 0; width: 600px; height: 190px; }
  .brand {
    position: absolute; left: 34px; top: 30px;
    display: flex; align-items: center; gap: 10px;
  }
  .brand-mark { width: 26px; height: 26px; background: var(--ink); }
  .brand-name {
    font-family: "Roboto Condensed", Arial, sans-serif;
    font-weight: 400; font-size: 42px; letter-spacing: 1px;
    color: var(--ink);
  }
  .offer-badge {
    position: absolute; left: 318px; top: -21px;
    width: 256px; height: 256px; border-radius: 50%;
    background: var(--pink);
    border: 9px solid var(--white);
    box-shadow: 0 4px 14px rgba(0,0,0,.3);
    display: flex; flex-direction: column; align-items: center; justify-content: center;
    font-family: "Roboto Condensed", Arial, sans-serif;
    color: var(--white); text-align: center; padding-top: 26px;
  }
  .offer-small { font-size: 40px; line-height: 1.05; }
  .offer-big { font-size: 58px; font-weight: 700; color: var(--yellow); line-height: 1.05; }
  .product-card {
    position: absolute; left: 62px; width: 472px; height: 212px;
  }
  .card-one { top: 131px; background: linear-gradient(90deg, var(--white) 30%, var(--peach) 100%); }
  .card-two { top: 364px; background: linear-gradient(90deg, var(--sky) 0%, var(--white) 75%); }
  .card-three { top: 596px; background: linear-gradient(90deg, var(--white) 35%, var(--blush) 100%); }
  .product-photo { position: absolute; border-radius: 50%; }
  .card-one .product-photo {
    left: 30px; top: 14px; width: 170px; height: 180px;
    background: radial-gradient(circle, #f1f1f1 0%, #d8b36a 60%, rgba(216,179,106,0) 72%);
  }
  .card-two .product-photo {
    left: 290px; top: 14px; width: 170px; height: 190px;
    background: radial-gradient(circle, #e44fa0 0%, #b9bfc7 55%, rgba(185,191,199,0) 72%);
  }
  .card-three .product-photo {
    left: 26px; top: 10px; width: 230px; height: 190px;
    background: radial-gradient(ellipse, #e86fa7 0%, #333 50%, rgba(51,51,51,0) 72%);
  }
  .product-name {
    position: absolute; font-size: 34px; font-weight: 300; color: var(--ink-soft);
  }
  .card-one .product-name { right: 20px; top: 140px; }
  .card-two .product-name { left: 20px; top: 134px; }
  .card-three .product-name { right: 20px; top: 130px; }
  .discount-tag {
    position: absolute; width: 64px; height: 96px;
    background: var(--pink); border-radius: 0 0 10px 10px;
    font-family: "Roboto Condensed", Arial, sans-serif;
    color: var(--yellow); text-align: center; font-size: 30px; line-height: 1.05;
    padding-top: 10px;
  }
  .discount-tag sup { font-size: 15px; }
  .card-two .discount-tag { left: 18px; top: 0; }
  .card-three .discount-tag { right: 18px; top: 0; }
  .cta-rule { position: absolute; top: 857px; height: 2px; width: 82px; background: var(--white); }
  .rule-left { left: 62px; }
  .rule-right { left: 452px; }
  .cta-button {
    position: absolute; left: 189px; top: 829px; width: 222px; height: 56px;
    border: 2px solid var(--white);
    display: flex; align-items: center; justify-content: center; gap: 12px;
    color: var(--yellow); font-size: 32px; font-weight: 400;
    text-decoration: none;
  }
  .cta-button svg { width: 32px; height: 20px; }
</style>
</head>
<body>
  <div class="banner">
    <svg class="header-wave" viewBox="0 0 600 190" aria-hidden="true">
      <path d="M0 0 H600 V120 C470 175 330 110 200 125 C110 135 50 150 0 150 Z" fill="#ffffff"/>
    </svg>

    <div class="brand">
      <span class="brand-mark"></span>
      <span class="brand-name">BRIMVALE</span>
    </div>

    <article class="product-card card-one">
      <div class="product-photo" role="img" aria-label="Gold ring with pavé diamonds and a solitaire stone"></div>
      <p class="product-name">Name Here</p>
    </article>

    <article class="product-card card-two">
      <div class="discount-tag">80<sup>%</sup><br>OFF</div>
      <p class="product-name">Name Here</p>
      <div class="product-photo" role="img" aria-label="Silver ring with pink and blue gemstones"></div>
    </article>

    <article class="product-card card-three">
      <div class="product-photo" role="img" aria-label="Black bridal ring set with a pink centre stone"></div>
      <div class="discount-tag">80<sup>%</sup><br>OFF</div>
      <p class="product-name">Name Here</p>
    </article>

    <div class="offer-badge">
      <span class="offer-small">Up To</span>
      <span class="offer-big">80% OFF</span>
      <span class="offer-small">Retail</span>
    </div>

    <span class="cta-rule rule-left"></span>
    <a class="cta-button" href="#">View Now
      <svg viewBox="0 0 32 20" aria-hidden="true">
        <path d="M2 10 C8 2 24 2 30 10 C24 18 8 18 2 10 Z" fill="none" stroke="#ffe61a" stroke-width="2.5"/>
        <circle cx="16" cy="10" r="4.5" fill="#ffe61a"/>
      </svg>
    </a>
    <span class="cta-rule rule-right"></span>
  </div>
</body>
</html>
```